Wine label design for my wife. Wine called "The Mirabel"

I need a wine label face lift of one of my premium wines in my collection. My wine sells in Harbor Lark's all over the States. My current label is called The Mirabel (my wife's name) and the illustration of her eyes is done by a well know artist from South Africa. I do not have to use this illustration and therefor I attached several pictures of her and her eyes, even when she was a little girl. The wine's also made in South Africa. This is a premium wine that we only sell 2000 bottles per year. The wine sells at 60 usd per bottle, The current label is too white. I also think her eyes should look more at the person buying it, than away from them.

Target Market(s)

Top end wine buyers

Font styles to use
Decorative
Script

Requirements
Must have
• 'The Mirabel' must be on the label
An illustration must be on the label
Basically all the info that's on the current label must be on by law. As per Sample
Nice to have
• Maybe some ideas of her whole face?
Should not have
• any gold colour

```html
<!DOCTYPE html>
<html lang="en">
<head>
<meta charset="UTF-8">
<title>The Mirabel – Sauvignon Blanc 2017 Label</title>
<link rel="stylesheet" href="https://fonts.googleapis.com/css2?family=Mrs+Saint+Delafield&family=Cormorant+Garamond:wght@500;600&display=swap">
<style>
  :root {
    --wine-red: #8b2a2e;
    --wine-red-deep: #7a2226;
    --shadow-grey: #a9a9a9;
    --paper: #ffffff;
  }
  * { margin: 0; padding: 0; box-sizing: border-box; }
  html, body {
    width: 1200px;
    height: 1000px;
    overflow: hidden;
    background: var(--paper);
  }
  .label {
    position: relative;
    width: 1200px;
    height: 1000px;
    background: var(--paper);
    color: var(--wine-red);
  }
  .label__title {
    position: absolute;
    top: 40px;
    left: 0;
    width: 100%;
    text-align: center;
    font-family: "Mrs Saint Delafield", cursive;
    font-weight: 400;
    font-size: 250px;
    line-height: 1;
    color: var(--wine-red);
    letter-spacing: 2px;
  }
  .label__varietal {
    position: absolute;
    top: 348px;
    left: 0;
    width: 100%;
    text-align: center;
    font-family: "Cormorant Garamond", serif;
    font-weight: 600;
    font-size: 54px;
    letter-spacing: 7px;
    line-height: 1;
    color: var(--wine-red);
  }
  .label__illustration {
    position: absolute;
    top: 428px;
    left: 140px;
    width: 920px;
    height: 400px;
  }
  .label__illustration svg {
    display: block;
    width: 100%;
    height: 100%;
  }
  .label__producer {
    position: absolute;
    top: 884px;
    left: 0;
    width: 100%;
    text-align: center;
    font-family: "Cormorant Garamond", serif;
    font-weight: 600;
    font-size: 68px;
    letter-spacing: 8px;
    line-height: 1;
    color: var(--wine-red);
  }
</style>
</head>
<body>
  <main class="label">
    <h1 class="label__title">The Mirabel</h1>
    <p class="label__varietal">SAUVIGNON BLANC 2017</p>
    <div class="label__illustration">
      <svg viewBox="0 0 920 400" role="img" aria-label="Sketched illustration of a woman's eyes and brows in wine red with grey shading">
        <defs>
          <linearGradient id="illustration-tone" x1="0" y1="0" x2="1" y2="1">
            <stop offset="0" stop-color="#8b2a2e" stop-opacity="0.85"/>
            <stop offset="0.55" stop-color="#a9a9a9" stop-opacity="0.75"/>
            <stop offset="1" stop-color="#7a2226" stop-opacity="0.9"/>
          </linearGradient>
        </defs>
        <rect x="0" y="0" width="920" height="400" fill="url(#illustration-tone)"/>
      </svg>
    </div>
    <p class="label__producer">ELIAS VARROW WINES</p>
  </main>
</body>
</html>
```